Information One Page for Email

I am looking for a informative attachment I can send with an introductive email for Ridgeview Cable Works. Something I can also Mail.

Ridgeview Cable Works is the leader in Rebar Post Tension Cable Placement and Post Tension Cable repair. Outside of cable placement and repair we do concrete repair, Parking Garage restoration and

Content

Post Tension Repair and Concrete Restoration
Post-tensioning is a revolutionary method in concrete construction that enhances the strength and durability of structures. However, like all construction ele-ments, post-tension cables can experience wear and damage over time. Ensuring timely and effective repair is crucial for maintaining the safety and integrity of your building.
Why Post-Tension Cable Repair is Essential
1. **Structural Integrity**: Damaged or deteriorated cables can compromise the structural integrity of your building, leading to safety hazards and potential structural failures.
2. **Extended Lifespan**: Regular maintenance and repair of post-tension cables extend the lifespan of your structure, ensuring it remains safe and function-al for years to come.
3. **Cost-Effective**: Addressing cable issues early on prevents more severe damage and costly repairs down the line.
Common Signs of Post-Tension Cable Issues
- Cracks in concrete surfaces
- Unusual noises or popping sounds
- Visible cable ends or broken strands
- Water leakage through cracks
Our Repair Process
1. **Inspection and Assessment**: Our team conducts a thorough inspection to identify the extent of the damage and determine the appropriate repair meth-ods.
2. **Cable Repair or Replacement**: Depending on the severity, we either re-pair the existing cables or replace them with new ones to restore full functional-ity.
3. **Sealing and Protection**: After repairing, we seal the affected areas to protect against moisture and future damage.
4. **Quality Assurance**: We perform rigorous quality checks to ensure the repairs meet industry standards and the structure is safe for use.
Why Choose Us
- **Expertise and Experience**: With years of experience in post-tension cable repair, our team is skilled in handling even the most complex repairs efficiently and effectively.
- **Advanced Technology**: We use the latest technology and materials to ensure durable and long-lasting repairs.
- **Customer Satisfaction**: Our commitment to quality and customer satisfaction sets us apart. We work closely with our clients to ensure their needs are met and expectations exceeded.
Contact Us
If you suspect issues with your post-tension cables or need a routine inspection, don't hesitate to contact us. Our experts are ready to provide the best solutions to keep your structures safe and secure.
Ensure the safety and longevity of your building with our professional post-tension cable repair services. Trust us to deliver quality and reliability every time.

```html
<!DOCTYPE html>
<html lang="en">
<head>
<meta charset="utf-8">
<title>Ridgeview Cable Works – Post Tension Repair</title>
<link href="https://fonts.googleapis.com/css2?family=Anton&family=Barlow:wght@600;700&family=Manrope:wght@400;500;600;700&display=swap" rel="stylesheet">
<style>
:root{
  --green:#1a6a3e;
  --green-dark:#155a34;
  --ink:#4a4a4a;
  --panel:#e6e7e8;
  --charcoal:#414042;
  --backdrop:#a7a7a7;
  --white:#ffffff;
}
*{box-sizing:border-box;margin:0;padding:0}
html,body{width:1200px;height:2238px;overflow:hidden;background:var(--backdrop)}
body{position:relative;font-family:"Manrope",sans-serif;color:var(--ink)}
.page{position:absolute;left:206px;width:788px;height:1019px;background:var(--white);overflow:hidden}
.page-front{top:76px}
.page-back{top:1136px}
.abs{position:absolute}

/* front */
.hero{left:0;top:0;width:788px;height:437px;background:linear-gradient(100deg,#ffffff 0%,#e4f3fb 25%,#cfe8f5 40%,rgba(207,232,245,0) 42%)}
.hero-photo{left:300px;top:0;width:488px;height:437px;background:linear-gradient(115deg,rgba(200,225,238,0) 0%,#c9ced0 22%,#b9b7b0 55%,#8f8a80 100%)}
.brand{left:62px;top:40px;display:flex;align-items:center;gap:10px;font-weight:700;font-size:24px;color:var(--green);line-height:1.1}
.brand-mark{width:14px;height:14px;background:var(--green)}
.headline{left:62px;top:150px;font-family:"Anton",sans-serif;font-size:55px;line-height:64px;color:var(--green);font-weight:400}
.intro{left:0;top:437px;width:788px;height:129px;background:var(--green);padding:17px 62px 0;color:var(--white);font-size:14.2px;line-height:23.2px}
.intro b{font-weight:700}
.photo-top{left:0;top:566px;width:408px;height:234px;background:linear-gradient(180deg,#c7c9cb,#a7a8a6 60%,#8a8883)}
.photo-bottom{left:0;top:804px;width:408px;height:203px;background:linear-gradient(180deg,#a9a49a,#d7d3cb 50%,#7b786f)}
.url-bar{left:0;top:963px;width:350px;height:44px;background:var(--charcoal);color:var(--white);font-weight:700;font-size:19px;padding:8px 62px}
.base-bar{left:0;top:1007px;width:788px;height:12px;background:var(--charcoal)}
.why-panel{left:408px;top:566px;width:380px;height:441px;background:var(--panel)}
.why-title{left:458px;top:588px;font-weight:700;font-size:21.5px;line-height:26px;color:var(--green)}
.reason{left:458px;width:290px}
.reason h3{font-size:14px;font-weight:700;color:var(--green);margin-bottom:7px}
.reason p{font-size:13.4px;line-height:18.5px}
.badge{width:58px;height:58px;border-radius:50%;background:var(--green);border:4px solid var(--white);box-shadow:0 0 0 1px #d4d4d4;display:flex;align-items:center;justify-content:center}
.badge svg{width:28px;height:28px}

/* back */
.signs-band{left:0;top:0;width:788px;height:333px;background:var(--green)}
.worker-photo{left:368px;top:0;width:420px;height:366px;background:linear-gradient(90deg,var(--green) 0%,#5b7d63 30%,#c7c2b5 65%,#b6ad9c 100%)}
.signs{left:69px;top:45px;color:var(--white)}
.signs h2{font-size:15.5px;font-weight:700;line-height:21px;margin-bottom:12px}
.signs li{list-style:none;font-size:13.8px;font-weight:600;height:28px;display:flex;align-items:center}
.signs li::before{content:"";width:0;height:0;border-left:8px solid var(--white);border-top:5px solid transparent;border-bottom:5px solid transparent;margin-right:24px}
.process{left:42px;top:224px;width:700px;height:307px;background:var(--panel);border-radius:18px;border-bottom:5px solid var(--green)}
.process-title{left:0;top:10px;width:700px;text-align:center;font-weight:700;font-size:21.5px;color:var(--green)}
.step{width:230px}
.step h3{font-size:13.8px;font-weight:700;color:var(--green);margin-bottom:7px}
.step p{font-size:13.4px;line-height:18.5px}
.step-icon{width:50px;height:50px;border-radius:50%;background:var(--green);display:flex;align-items:center;justify-content:center}
.step-icon svg{width:28px;height:28px}
.choose-title{left:0;top:549px;width:788px;text-align:center;font-weight:700;font-size:21.5px;color:var(--green)}
.choose{width:190px;text-align:center}
.choose .tick{width:19px;height:19px;margin:0 auto 10px;display:block}
.choose h3{font-size:13.8px;font-weight:700;color:var(--green);margin-bottom:7px}
.choose p{font-size:13.4px;line-height:18.5px}
.divider{top:583px;width:1.5px;height:160px;background:var(--green)}
.call{left:0;top:760px;width:788px;text-align:center;font-family:"Barlow",sans-serif;font-weight:700;font-size:76px;line-height:90px;color:var(--green)}
.visit{left:0;top:862px;width:788px;text-align:center;font-family:"Barlow",sans-serif;font-weight:700;font-size:25px;color:var(--green)}
.tagline{left:0;top:901px;width:788px;text-align:center;font-size:14px;letter-spacing:4px;color:var(--ink)}
.footer{left:0;top:937px;width:788px;height:82px;background:var(--charcoal);color:var(--white);font-size:9.6px;line-height:13.6px;padding:15px 62px 0}
</style>
</head>
<body>

<section class="page page-front">
  <div class="abs hero"></div>
  <div class="abs hero-photo" role="img" aria-label="Concrete balconies of a high-rise shored with temporary posts during restoration"></div>
  <div class="abs brand"><span class="brand-mark"></span>Ridgeview Cable Works</div>
  <h1 class="abs headline">Post Tension<br>Repair and<br>Concrete<br>Restoration</h1>

  <p class="abs intro"><b>Post-tensioning</b> is a revolutionary method in concrete construction that enhancesthe strength and durability of structures. However, like all construction ele-ments, post-tension cables can experience wear and damage over time. Ensuring timely and effective repair is crucial for maintaining the safety and integrity of your building.</p>

  <div class="abs photo-top" role="img" aria-label="Parking deck of a coastal condominium tower"></div>
  <div class="abs photo-bottom" role="img" aria-label="Building facade with patched concrete balconies under repair"></div>
  <div class="abs url-bar">ridgeviewcableworks.com</div>

  <div class="abs why-panel"></div>
  <h2 class="abs why-title">WHY POST-TENSION CABLE<br>REPAIR IS ESSENTIAL</h2>

  <div class="abs badge" style="left:379px;top:649px">
    <svg viewBox="0 0 28 28" fill="none" stroke="#fff" stroke-width="1.8"><path d="M5 24h18M7 24V14M12 24V14M16 24V14M21 24V14M4 14h20M6 10h16M10 6h8"/></svg>
  </div>
  <div class="abs reason" style="top:651px">
    <h3>Structural Integrity</h3>
    <p>Damaged or deteriorated cables can compromise the structural integrity of your building, leading to safety hazards and potential structural failures.</p>
  </div>

  <div class="abs badge" style="left:379px;top:770px">
    <svg viewBox="0 0 28 28" fill="none" stroke="#fff" stroke-width="1.8"><rect x="9" y="9" width="10" height="10"/><path d="M3 8V3h5M20 3h5v5M25 20v5h-5M8 25H3v-5"/></svg>
  </div>
  <div class="abs reason" style="top:771px">
    <h3>Extended Lifespan</h3>
    <p>Regular maintenance and repair of post-tension cables extend the lifespan of your structure, ensuring it remains safe and function-al for years to come.</p>
  </div>

  <div class="abs badge" style="left:379px;top:888px">
    <svg viewBox="0 0 28 28" fill="none" stroke="#fff" stroke-width="1.8"><circle cx="16" cy="11" r="6"/><path d="M16 8v6M3 20l5-3h6l6 3-9 5z"/></svg>
  </div>
  <div class="abs reason" style="top:888px">
    <h3>Cost-Effective</h3>
    <p>Addressing cable issues early on prevents more severe damage and costly repairs down the line.</p>
  </div>

  <div class="abs base-bar"></div>
</section>

<section class="page page-back">
  <div class="abs signs-band"></div>
  <div class="abs worker-photo" role="img" aria-label="Worker with a jackhammer removing damaged concrete from a balcony slab"></div>
  <div class="abs signs">
    <h2>Common Signs of Post-Tension<br>Cable Issues</h2>
    <ul>
      <li>Cracks in concrete surfaces</li>
      <li>Unusual noises or popping sounds</li>
      <li>Visible cable ends or broken strands</li>
      <li>Water leakage through cracks</li>
    </ul>
  </div>

  <div class="abs process">
    <h2 class="abs process-title">OUR REPAIR PROCESS</h2>

    <div class="abs step-icon" style="left:27px;top:60px">
      <svg viewBox="0 0 28 28" fill="none" stroke="#fff" stroke-width="1.8"><circle cx="15" cy="12" r="8"/><path d="M11 12l3 3 5-6M9 18l-6 6"/></svg>
    </div>
    <div class="abs step" style="left:100px;top:60px">
      <h3>Inspection and Assessment</h3>
      <p>Our team conducts a thorough inspection to identify the extent of the damage and determine the appropriate repair meth-ods.</p>
    </div>

    <div class="abs step-icon" style="left:365px;top:60px">
      <svg viewBox="0 0 28 28" fill="none" stroke="#fff" stroke-width="1.8"><path d="M14 3l9 3v7c0 6-4 10-9 12-5-2-9-6-9-12V6z"/><path d="M10 14l3 3 5-6"/></svg>
    </div>
    <div class="abs step" style="left:438px;top:60px">
      <h3>Sealing and Protection</h3>
      <p>After repairing, we seal the affected areas to protect against moisture and future damage.</p>
    </div>

    <div class="abs step-icon" style="left:27px;top:185px">
      <svg viewBox="0 0 28 28" fill="none" stroke="#fff" stroke-width="1.8"><path d="M4 22c6 0 4-8 10-8s4-8 10-8M14 3v3M19 5l-2 2M9 5l2 2M5 14h3M20 22h3"/></svg>
    </div>
    <div class="abs step" style="left:100px;top:185px">
      <h3>Cable Repair or Replacemen</h3>
      <p>Depending on the severity, we either re-pair the existing cables or replace them with new ones to restore full functional-ity.</p>
    </div>

    <div class="abs step-icon" style="left:365px;top:185px">
      <svg viewBox="0 0 28 28" fill="none" stroke="#fff" stroke-width="1.8"><circle cx="14" cy="14" r="10"/><circle cx="14" cy="14" r="6"/><path d="M11 14l2 2 4-4"/></svg>
    </div>
    <div class="abs step" style="left:438px;top:185px">
      <h3>Quality Assurance</h3>
      <p>We perform rigorous quality checks to ensure the repairs meet industry standards and the structure is safe for use.</p>
    </div>
  </div>

  <h2 class="abs choose-title">WHY CHOOSE US</h2>
  <div class="abs divider" style="left:262px"></div>
  <div class="abs divider" style="left:526px"></div>

  <div class="abs choose" style="left:59px;top:573px">
    <svg class="tick" viewBox="0 0 20 20"><circle cx="10" cy="10" r="10" fill="#1a6a3e"/><path d="M5.5 10.5l3 3 6-6" fill="none" stroke="#fff" stroke-width="2"/></svg>
    <h3>Expertise and Experience</h3>
    <p>With years of experience in post-tension cable repair, our team is skilled in handling even the most complex repairs efficiently and effectively.</p>
  </div>
  <div class="abs choose" style="left:299px;top:573px">
    <svg class="tick" viewBox="0 0 20 20"><circle cx="10" cy="10" r="10" fill="#1a6a3e"/><path d="M5.5 10.5l3 3 6-6" fill="none" stroke="#fff" stroke-width="2"/></svg>
    <h3>Customer Satisfaction</h3>
    <p>Our commitment to quality and customer satisfaction sets us apart. We work closely with our clients to ensure their needs are met and expectations exceeded.</p>
  </div>
  <div class="abs choose" style="left:544px;top:573px">
    <svg class="tick" viewBox="0 0 20 20"><circle cx="10" cy="10" r="10" fill="#1a6a3e"/><path d="M5.5 10.5l3 3 6-6" fill="none" stroke="#fff" stroke-width="2"/></svg>
    <h3>Advanced Technology</h3>
    <p>We use the latest technology and materials to ensure durable and long-lasting repairs.</p>
  </div>

  <div class="abs call">CALL (555) 014-2290</div>
  <div class="abs visit">AND VISIT WWW.RIDGEVIEWCABLEWORKS.COM</div>
  <div class="abs tagline">TO START YOUR CONSTRUCTION PROJECT!</div>

  <p class="abs footer">If you suspect issues with your post-tension cables or need a routine inspection, don't hesitate to contact us. Our experts are ready to provide the best solutions to keep your structures safe and secure. Ensure the safety and longevity of your building with our professional post-tension cable repair services. Trust us to deliver quality and reliability every time.</p>
</section>

</body>
</html>
```